BrightLoop (1 page) homepage re-design

Our homepage needs a face-lift! We need our homepage on our website re-designed with a fresh and current look and feel. We have all the details, colour codes and a rough wireframe ready, but need a talented designer to put some personality into our ideas.

What we do: BrightLoop is a digital marketing agency with offices in Australia (Sydney) and South Africa (Cape Town). We specialise in SEO, PPC (otherwise known as Zentro PayLine or SEM), content marketing and Zentro Tallyboard. We use these tools to help our clients realise their business dreams.

VISUAL

Style / theme of the design:
Clean, simplistic, fun, flow.

Websites we draw inspiration from:
This is the theme we want to use to build the website
http://demo.vormalayouts.example/vl/?theme=Pebbled
Inspiration:
https://www.ondrapromo.example/
https://www.nelvagrowth.example.au/
https://quimbel.example.au/
https://torvin.layout-works.example/forum/

What we like about the site:
Clean, simple design, good use of white space. The subtle changing background colours, strong contrast with text. Not too busy or distracting.

What we don’t want: Too many different colours.

Target Market(s)

Our target audience: Marketing Managers of small to medium size businesses in Australia.

Industry/Entity Type

Marketing

Number of Pages Required

1 page

Font styles to use
Sans Serif

Requirements
Must have
• Elements to be added on homepage in order and as seen in attachments:
• - Section 1: Video with team as image and a play button add the heading: We help smart marketing managers achieve their KPIs [line break] and reduce their digital marketing overwhelm.
• - Section 2: Solutions section with the 6 solutions displayed in a row.
• - Section 3: Register Free Webinar with video
• - Section 4: Please add 3 case studies (as seen in attached docs there is only 1 but please add 3 below each other)
• - Section 5: Clients. Please add all client logo’s (black and white)
• - Section 6: Our Blog (as seen attached)
• - Section 7: Conferences Attended (please add the title and a paragraph of lorem Ipsom below) and then please add all conference logo’s attached below.
• - Section 8: In The Media (please add all logo’s titled media) white background
• - Section 9: Footer (dark grey footer) add our Zentro honoured affiliate logo here please
• - Section10: Footer - include:
• - Social logos (WorkMesh, Blipster, Pallwall, ReelDrop, Zentro Hub)
• - Navigation
• - Contact details (name, address, phone number, email)
• Colour codes:
• We want to use light greys, white and charcoal grey for the backgrounds with a pop of our green colour to bring out our branding and all CTA’s to be orange, colour codes below:
• Light grey: #F2F2F2
• Charcoal grey: #161616
• Green: #428E29
• CTA’s: #de7532
• PLEASE NOTE: Please see attached pdf titled: homepagecopybrief.pdf for all the titles and statistics that need to go on the homepage
Should not have
• Too much colour, icons should not be different colours

```html
<!DOCTYPE html>
<html lang="en">
<head>
<meta charset="utf-8">
<title>BrightLoop — Digital Marketing Agency</title>
<link href="https://fonts.googleapis.com/css2?family=Oswald:wght@300;400;500;600&family=Open+Sans:wght@400;600;700&display=swap" rel="stylesheet">
<style>
:root{
  --green:#428E29;
  --green-dark:#37791f;
  --orange:#de7532;
  --charcoal:#161616;
  --dark:#222222;
  --light:#F2F2F2;
  --white:#ffffff;
  --text:#555555;
  --muted:#8a8a8a;
  --link:#2f6fb4;
  --head:'Oswald',sans-serif;
  --body:'Open Sans',sans-serif;
}
*{box-sizing:border-box;margin:0;padding:0}
html,body{width:1200px;height:3896px;overflow:hidden}
body{position:relative;background:var(--white);font-family:var(--body);color:var(--text)}
.abs{position:absolute}
.section-title{position:absolute;left:0;width:1200px;text-align:center;font-family:var(--head);font-weight:500;font-size:24px;letter-spacing:.5px;color:var(--dark);text-transform:uppercase}
.section-intro{position:absolute;left:350px;width:500px;text-align:center;font-size:11px;line-height:18px;color:var(--text)}
.on-green{color:var(--white)}
.btn{display:inline-block;font-family:var(--head);font-size:11px;letter-spacing:.5px;color:var(--white);background:var(--orange);border-radius:14px;padding:5px 14px;text-transform:uppercase}

/* header / hero */
.hero-photo{left:0;top:0;width:1200px;height:600px;background:linear-gradient(180deg,#3a3a3a 0%,#5b5b5b 35%,#4a4a4a 70%,#2e2e2e 100%)}
.hero-shade{left:0;top:0;width:1200px;height:600px;background:rgba(0,0,0,.25)}
.site-nav{left:0;top:0;width:1200px;height:52px}
.brand{left:229px;top:12px;display:flex;align-items:center;gap:6px;font-family:var(--head);font-weight:500;font-size:20px;letter-spacing:1px;color:var(--white);text-transform:uppercase}
.brand-square{width:14px;height:14px;background:var(--green)}
.menu{left:499px;top:17px;width:468px;display:flex;justify-content:space-between;font-family:var(--head);font-size:11px;letter-spacing:.5px;color:var(--white)}
.menu .active{color:var(--orange)}
.play{width:64px;height:64px;border-radius:50%;background:rgba(255,255,255,.35);display:flex;align-items:center;justify-content:center}
.hero-play{left:568px;top:259px}
.hero-heading{left:0;top:398px;width:1200px;text-align:center;font-family:var(--head);font-weight:500;font-size:27px;line-height:33px;color:var(--white);text-transform:uppercase;letter-spacing:.5px}
.hero-wave{left:0;top:520px}

/* needs */
.needs-grid{left:236px;top:770px;width:730px;display:grid;grid-template-columns:repeat(3,240px);column-gap:5px;row-gap:0}
.need{height:222px;text-align:center;padding-top:20px}
.need.featured{background:var(--white);box-shadow:0 0 18px rgba(0,0,0,.12)}
.need-icon{width:58px;height:58px;margin:0 auto;border-radius:50%;border:1px solid #e3e3e3;display:flex;align-items:center;justify-content:center}
.need h3{margin-top:22px;font-family:var(--head);font-weight:500;font-size:13px;color:var(--dark);text-transform:uppercase;letter-spacing:.3px}
.need p{margin:8px auto 0;width:176px;font-size:9.5px;line-height:14px;color:var(--text)}
.need .more{display:block;margin-top:8px;font-family:var(--head);font-size:10px;color:var(--orange);text-transform:uppercase}

/* webinar */
.webinar{left:0;top:1257px;width:1200px;height:322px;background:var(--green)}
.webinar-kicker{left:229px;top:35px;font-family:var(--head);font-weight:300;font-size:44px;line-height:48px;color:var(--white);letter-spacing:1px}
.webinar-title{left:227px;top:78px;font-family:var(--head);font-weight:600;font-size:96px;line-height:104px;color:var(--white);letter-spacing:2px}
.webinar-text{left:229px;top:188px;width:320px;font-size:10.5px;line-height:16px;color:var(--white)}
.webinar-btn{left:229px;top:249px;width:127px;height:31px;border:1.5px solid var(--white);border-radius:16px;font-family:var(--head);font-size:12px;color:var(--white);display:flex;align-items:center;justify-content:center;letter-spacing:.5px}
.webinar-video{left:608px;top:41px;width:358px;height:240px;border:4px solid var(--white);background:linear-gradient(135deg,#8a8a86 0%,#6f6a66 45%,#9b8b86 100%)}
.webinar-play{left:143px;top:84px}

/* cards */
.card-row{left:231px;width:736px;display:grid;grid-template-columns:repeat(3,235px);column-gap:15px}
.case{position:relative;height:218px;background:linear-gradient(160deg,#6b6b6b 0%,#4b4b4b 60%,#3a3a3a 100%);overflow:hidden}
.case::after{content:"";position:absolute;inset:0;background:linear-gradient(180deg,rgba(0,0,0,0) 35%,rgba(0,0,0,.6) 100%)}
.case-body{position:absolute;left:14px;bottom:14px;z-index:1;color:var(--white)}
.case-body h3{font-family:var(--head);font-weight:500;font-size:13px;letter-spacing:.4px}
.case-body p{margin:5px 0 10px;width:170px;font-size:9.5px;line-height:13px}

/* clients */
.clients{left:0;top:1989px;width:1200px;height:440px;background:var(--green)}
.logo-grid{display:grid;grid-template-columns:repeat(5,135px);column-gap:13px;row-gap:15px}
.logo-tile{height:115px;background:var(--white);display:flex;align-items:center;justify-content:center;gap:7px;font-family:var(--body);font-weight:600;font-size:13px;color:#7a7a7a;text-align:center;padding:0 8px;white-space:nowrap}
.mark-dot{width:10px;height:10px;border-radius:50%;background:#9a9a9a;flex:none}

/* blog */
.post{height:268px;background:var(--white);border:1px solid #e6e6e6}
.post-photo{position:relative;height:135px;background:linear-gradient(150deg,#5e5a57 0%,#3f3c3a 60%,#6c6661 100%)}
.post-meta{position:absolute;right:10px;bottom:8px;font-family:var(--head);font-size:9px;color:var(--white);letter-spacing:.3px}
.post h3{margin:14px 16px 0;font-family:var(--head);font-weight:500;font-size:12px;color:var(--link);text-transform:uppercase}
.post p{margin:8px 16px 0;font-size:9.5px;line-height:13.5px;color:var(--text)}
.post-share{margin:12px 16px 0;padding-top:8px;border-top:1px solid #eeeeee;display:flex;gap:10px;font-size:8px;color:var(--muted);text-transform:uppercase}
.post-share .on{color:var(--link)}
.post-share .more{margin-left:auto;text-transform:none}
.dots{left:0;top:2905px;width:1200px;display:flex;justify-content:center;gap:6px}
.dots span{width:8px;height:8px;border-radius:50%;background:#d6d6d6}
.dots span.on{background:var(--muted)}

/* learning */
.learning{left:0;top:2960px;width:1200px;height:262px;background:linear-gradient(180deg,#4a9a30 0%,var(--green) 100%)}
.learning-logos .logo-tile{height:66px;font-size:14px}

/* media */
.media-grid{left:235px;top:3342px;width:732px;display:grid;grid-template-columns:repeat(6,110px);column-gap:14px}
.media-tile{height:94px;background:var(--light);display:flex;align-items:center;justify-content:center;font-family:var(--body);font-weight:700;font-size:13px;color:#333333;text-align:center;padding:0 6px;white-space:nowrap}

/* footer */
.footer{left:0;top:3478px;width:1200px;height:418px}
.enquiry-icon{left:574px;top:3546px;width:52px;height:52px;border-radius:50%;border:2px solid var(--orange);display:flex;align-items:center;justify-content:center;font-family:var(--head);font-size:15px;color:var(--orange)}
.enquiry-label{left:0;top:3607px;width:1200px;text-align:center;font-family:var(--head);font-size:13px;color:var(--orange);letter-spacing:.5px}
.enquiry-phone{left:0;top:3626px;width:1200px;text-align:center;font-family:var(--head);font-weight:500;font-size:30px;color:var(--orange);letter-spacing:1px}
.foot-col h4{font-family:var(--head);font-weight:500;font-size:14px;color:var(--white);text-transform:uppercase;letter-spacing:.5px;margin-bottom:12px}
.foot-col li{list-style:none;font-size:9.5px;line-height:17px;color:#bdbdbd}
.foot-col .split{display:flex;gap:36px}
.contact-line{display:flex;gap:8px;align-items:flex-start;font-size:9.5px;line-height:14px;color:#bdbdbd;margin-bottom:10px}
.foot-bar{left:231px;top:3860px;width:736px;height:28px;display:flex;align-items:center;justify-content:space-between;font-size:9px;color:#bdbdbd}
.socials{display:flex;gap:9px}
.socials span{width:14px;height:14px;border-radius:50%;border:1px solid #bdbdbd}
</style>
</head>
<body>

<!-- hero -->
<div class="abs hero-photo" role="img" aria-label="Team photo of the BrightLoop staff standing together, used as video poster"></div>
<div class="abs hero-shade"></div>
<header class="abs site-nav">
  <div class="abs brand"><span class="brand-square"></span>BrightLoop</div>
  <nav class="abs menu">
    <span class="active">HOME</span><span>ABOUT</span><span>PPC</span><span>SEO</span><span>TRAINING</span><span>CLIENT</span><span>SUCCESS</span><span>BLOG</span><span>RESOURCES</span><span>CONTACT</span>
  </nav>
</header>
<div class="abs play hero-play"><svg width="22" height="26" viewBox="0 0 22 26"><path d="M2 1 L21 13 L2 25 Z" fill="#ffffff"/></svg></div>
<h1 class="abs hero-heading">We help smart marketing managers achieve their KPIs<br>and reduce their digital marketing overwhelm</h1>
<svg class="abs hero-wave" width="1200" height="82" viewBox="0 0 1200 82" preserveAspectRatio="none"><path d="M0 70 C200 40 360 40 560 62 C760 84 980 60 1200 20 L1200 82 L0 82 Z" fill="#ffffff"/></svg>

<!-- needs -->
<h2 class="section-title" style="top:664px">Which box best describes your needs?</h2>
<p class="section-intro" style="top:700px">Lorem Ipsum is simply dummy text of the printing and typesetting industry. Lorem Ipsum has been the industry's standard dummy text ever since the 1500s.</p>
<div class="abs needs-grid">
  <div class="need">
    <div class="need-icon"><svg width="28" height="28" viewBox="0 0 28 28" fill="none" stroke="#428E29" stroke-width="1.6"><path d="M4 24h20M7 24v-6M12 24v-10M17 24v-8M22 24v-14M6 12l6-5 5 3 6-6"/></svg></div>
    <h3>Grow Revenue</h3>
    <p>Lorem Ipsum is simply dummy text of the printing and typesetting industry. Lorem Ipsum has been the industry's standard dummy.</p>
    <span class="more">Read More</span>
  </div>
  <div class="need">
    <div class="need-icon"><svg width="28" height="28" viewBox="0 0 28 28" fill="none" stroke="#428E29" stroke-width="1.6"><path d="M7 4v20M14 4v20M21 4v20"/><rect x="4.5" y="8" width="5" height="4"/><rect x="11.5" y="15" width="5" height="4"/><rect x="18.5" y="10" width="5" height="4"/></svg></div>
    <h3>Convert Leads</h3>
    <p>Lorem Ipsum is simply dummy text of the printing and typesetting industry. Lorem Ipsum has been the industry's standard dummy.</p>
    <span class="more">Read More</span>
  </div>
  <div class="need">
    <div class="need-icon"><svg width="28" height="28" viewBox="0 0 28 28" fill="none" stroke="#428E29" stroke-width="1.6"><path d="M5 11v6h4l9 5V6l-9 5H5zM9 17l2 6h3l-2-6M21 11c2 1 2 5 0 6"/></svg></div>
    <h3>Increase Brand Awareness</h3>
    <p>Lorem Ipsum is simply dummy text of the printing and typesetting industry. Lorem Ipsum has been the industry's standard dummy.</p>
    <span class="more">Read More</span>
  </div>
  <div class="need">
    <div class="need-icon"><svg width="28" height="28" viewBox="0 0 28 28" fill="none" stroke="#428E29" stroke-width="1.6"><path d="M7 4h10l5 5v15H7zM17 4v5h5M10 14h9M10 18h9M10 22h6"/></svg></div>
    <h3>Data / KAPI's</h3>
    <p>Lorem Ipsum is simply dummy text of the printing and typesetting industry. Lorem Ipsum has been the industry's standard dummy.</p>
    <span class="more">Read More</span>
  </div>
  <div class="need featured">
    <div class="need-icon"><svg width="28" height="28" viewBox="0 0 28 28" fill="none" stroke="#428E29" stroke-width="1.6"><circle cx="14" cy="14" r="3"/><circle cx="6" cy="6" r="2.5"/><circle cx="22" cy="6" r="2.5"/><circle cx="6" cy="22" r="2.5"/><circle cx="22" cy="22" r="2.5"/><path d="M8 8l4 4M20 8l-4 4M8 20l4-4M20 20l-4-4"/></svg></div>
    <h3>Increase Engagement</h3>
    <p>Lorem Ipsum is simply dummy text of the printing and typesetting industry. Lorem Ipsum has been the industry's standard dummy.</p>
    <span class="more">Read More</span>
  </div>
  <div class="need">
    <div class="need-icon"><svg width="28" height="28" viewBox="0 0 28 28" fill="none" stroke="#428E29" stroke-width="1.6"><rect x="4" y="5" width="20" height="15"/><path d="M4 9h20M14 20v4M9 24h10"/></svg></div>
    <h3>Marketing Strategy / Budgeting</h3>
    <p>Lorem Ipsum is simply dummy text of the printing and typesetting industry. Lorem Ipsum has been the industry's standard dummy.</p>
    <span class="more">Read More</span>
  </div>
</div>

<!-- webinar -->
<section class="abs webinar">
  <div class="abs webinar-kicker">FREE REGISTER</div>
  <div class="abs webinar-title">WEBINAR</div>
  <p class="abs webinar-text">Lorem Ipsum is simply dummy text of the printing and typesetting industry. Lorem Ipsum has been the industry's standard dummy. Lorem Ipsum is simply dummy text.</p>
  <div class="abs webinar-btn">REGISTER NOW</div>
  <div class="abs webinar-video" role="img" aria-label="Webinar video still of a woman walking with shopping bags">
    <div class="abs play webinar-play"><svg width="22" height="26" viewBox="0 0 22 26"><path d="M2 1 L21 13 L2 25 Z" fill="#ffffff"/></svg></div>
  </div>
</section>

<!-- case studies -->
<h2 class="section-title" style="top:1623px">Our Case Study</h2>
<p class="section-intro" style="top:1659px">Lorem Ipsum is simply dummy text of the printing and typesetting industry. Lorem Ipsum has been the industry's standard dummy text ever since the 1500s.</p>
<div class="abs card-row" style="top:1719px">
  <div class="case" role="img" aria-label="Case study photo of hands working on a laptop"><div class="case-body"><h3>MRKLAWYERS</h3><p>Lorem Ipsum is simply dummy text of the printing and typesetting industry.</p><span class="btn">Read More</span></div></div>
  <div class="case" role="img" aria-label="Case study photo of a team reviewing documents at a desk"><div class="case-body"><h3>MRKLAWYERS</h3><p>Lorem Ipsum is simply dummy text of the printing and typesetting industry.</p><span class="btn">Read More</span></div></div>
  <div class="case" role="img" aria-label="Case study photo of a laptop showing analytics charts"><div class="case-body"><h3>MRKLAWYERS</h3><p>Lorem Ipsum is simply dummy text of the printing and typesetting industry.</p><span class="btn">Read More</span></div></div>
</div>

<!-- clients -->
<section class="abs clients"></section>
<svg class="abs" style="left:0;top:2380px" width="1200" height="80" viewBox="0 0 1200 80" preserveAspectRatio="none"><path d="M0 0 L1200 0 L1200 30 C1000 70 820 76 620 50 C420 24 220 40 0 72 Z" fill="#428E29"/></svg>
<h2 class="section-title on-green" style="top:2031px">Our Client</h2>
<p class="section-intro on-green" style="top:2067px">Lorem Ipsum is simply dummy text of the printing and typesetting industry. Lorem Ipsum has been the industry's standard dummy text ever since the 1500s.</p>
<div class="abs logo-grid" style="left:236px;top:2124px">
  <div class="logo-tile"><span class="mark-dot"></span>Clarion Sight</div>
  <div class="logo-tile">Tradeva</div>
  <div class="logo-tile">Pixelmoor</div>
  <div class="logo-tile">Holtby Storage</div>
  <div class="logo-tile"><span class="mark-dot"></span>Stillbrook</div>
  <div class="logo-tile">PriceCrate</div>
  <div class="logo-tile">KV Strategy</div>
  <div class="logo-tile">Outrangers</div>
  <div class="logo-tile">Precis</div>
  <div class="logo-tile">Northgate Co</div>
</div>

<!-- blog -->
<h2 class="section-title" style="top:2519px">Latest Blog</h2>
<p class="section-intro" style="top:2555px">Lorem Ipsum is simply dummy text of the printing and typesetting industry. Lorem Ipsum has been the industry's standard dummy text ever since the 1500s.</p>
<div class="abs card-row" style="top:2615px">
  <article class="post"><div class="post-photo" role="img" aria-label="Blog photo of a man working at a cafe table"><span class="post-meta">NOV 14 &nbsp; 20</span></div><h3>Lorem Ipsum is simply dummy</h3><p>Lorem Ipsum is simply dummy text of the printing and typesetting industry. Lorem Ipsum has been the industry's.</p><div class="post-share"><span>Pallwall</span><span class="on">Blipster</span><span>Zentro Hub</span><span class="more">More...</span></div></article>
  <article class="post"><div class="post-photo" role="img" aria-label="Blog photo of a city train platform"><span class="post-meta">NOV 14 &nbsp; 20</span></div><h3>Lorem Ipsum is simply dummy</h3><p>Lorem Ipsum is simply dummy text of the printing and typesetting industry. Lorem Ipsum has been the industry's.</p><div class="post-share"><span>Pallwall</span><span class="on">Blipster</span><span>Zentro Hub</span><span class="more">More...</span></div></article>
  <article class="post"><div class="post-photo" role="img" aria-label="Blog photo of a traveller on a railway platform"><span class="post-meta">NOV 14 &nbsp; 20</span></div><h3>Lorem Ipsum is simply dummy</h3><p>Lorem Ipsum is simply dummy text of the printing and typesetting industry. Lorem Ipsum has been the industry's.</p><div class="post-share"><span>Pallwall</span><span class="on">Blipster</span><span>Zentro Hub</span><span class="more">More...</span></div></article>
</div>
<div class="abs dots"><span></span><span></span><span></span><span class="on"></span><span></span></div>

<!-- learning / conferences -->
<section class="abs learning"></section>
<h2 class="section-title on-green" style="top:3005px">Learning</h2>
<p class="section-intro on-green" style="top:3046px;left:290px;width:620px">Lorem Ipsum is simply dummy text of the printing and typesetting industry. Lorem Ipsum has been the industry's standard dummy text ever since the 1500s, when an unknown printer took a galley of type and scrambled it to make a type specimen book. It has survived not only five centuries, but also the leap into electronic typesetting, remaining essentially unchanged.</p>
<div class="abs logo-grid learning-logos" style="left:236px;top:3137px">
  <div class="logo-tile"><span class="mark-dot"></span>Webmeet</div>
  <div class="logo-tile">Growth Forum</div>
  <div class="logo-tile">SRX Summit</div>
  <div class="logo-tile"><span class="mark-dot"></span>Liftpage</div>
  <div class="logo-tile">Upstream</div>
</div>

<!-- media -->
<h2 class="section-title" style="top:3246px">In The Media</h2>
<p class="section-intro" style="top:3282px">Lorem Ipsum is simply dummy text of the printing and typesetting industry. Lorem Ipsum has been the industry's standard dummy text ever since the 1500s.</p>
<div class="abs media-grid">
  <div class="media-tile">Tallowby</div>
  <div class="media-tile">Mindmeal</div>
  <div class="media-tile">Quillton Post</div>
  <div class="media-tile">myventure</div>
  <div class="media-tile">Wendale Herald</div>
  <div class="media-tile">Going Alone</div>
</div>

<!-- footer -->
<svg class="abs footer" width="1200" height="418" viewBox="0 0 1200 418" preserveAspectRatio="none"><path d="M0 30 C220 0 420 4 620 28 C820 52 1010 40 1200 10 L1200 418 L0 418 Z" fill="#161616"/></svg>
<div class="abs enquiry-icon">24</div>
<div class="abs enquiry-label">ANY ENQUIRY</div>
<div class="abs enquiry-phone">1300 555 010</div>

<div class="abs foot-col" style="left:231px;top:3706px;width:180px">
  <h4>Get In Touch</h4>
  <div class="contact-line"><svg width="10" height="12" viewBox="0 0 10 12"><path d="M5 0a4 4 0 0 1 4 4c0 3-4 8-4 8S1 7 1 4a4 4 0 0 1 4-4z" fill="#de7532"/></svg><span>12 Lorem Ipsum Street,<br>Harbour Business Park,<br>Sydney, 2000</span></div>
  <div class="contact-line"><svg width="10" height="10" viewBox="0 0 10 10"><path d="M2 0l2 2-1 2c1 1 2 2 3 3l2-1 2 2-2 2C4 10 0 6 0 2z" fill="#de7532"/></svg><span>0123 555 0190</span></div>
  <div class="contact-line"><svg width="11" height="9" viewBox="0 0 11 9"><rect width="11" height="9" fill="#de7532"/><path d="M0 0l5.5 5L11 0" stroke="#161616" fill="none"/></svg><span>hello@brightloop.example</span></div>
</div>
<div class="abs foot-col" style="left:436px;top:3706px">
  <h4>Information</h4>
  <div class="split">
    <ul><li>Home</li><li>About</li><li>PPC</li><li>SEO</li><li>Training</li></ul>
    <ul><li>Client</li><li>Success</li><li>Blog</li><li>Resources</li><li>Contact</li></ul>
  </div>
</div>
<div class="abs foot-col" style="left:657px;top:3706px">
  <h4>SEO</h4>
  <ul><li>SEO Management</li><li>SEO Audits</li><li>SEO Consulting</li><li>Penalty Recovery</li></ul>
</div>
<div class="abs foot-col" style="left:831px;top:3706px">
  <h4>Resources</h4>
  <ul><li>Podcasts</li><li>eBooks</li><li>Our Blog</li></ul>
</div>
<div class="abs foot-bar">
  <span>Copyright © 2018 BrightLoop</span>
  <div class="socials" aria-label="WorkMesh, Blipster, Pallwall, ReelDrop, Zentro Hub"><span></span><span></span><span></span><span></span><span></span></div>
</div>

</body>
</html>
```